Redesign and move to Wordpress for qorvanta.com

Our website needs a redesign and at the same time we are moving it to Wordpress. Please help us with a new digital professional look and feel.

We are an Australian Software Engineering company specialising in advanced software development using in A.I., PLatform Engineering, Integration and Cloud. See the current qorvanta.com for more information about us.

```html
<!DOCTYPE html>
<html lang="en">
<head>
<meta charset="utf-8">
<title>Qorvanta — Reliable Smart Software Engineering</title>
<link rel="stylesheet" href="https://fonts.googleapis.com/css2?family=Mulish:wght@400;600;700;800;900&family=Montserrat:wght@700;800&display=swap">
<style>
:root{
  --accent:#4fc4bd;
  --accent-soft:#7fd9d3;
  --hero-bg:#0f3a40;
  --band:#2e9590;
  --band-dark:#237c78;
  --deep:#0e5654;
  --ink:#111;
  --body:#2a2a2a;
  --footer:#12393d;
  --footer-bar:#0f4b4d;
  --slate:#4a5f7a;
  --tint:#eef4f4;
  --white:#fff;
}
*{box-sizing:border-box;margin:0;padding:0}
html,body{width:1200px;height:4191px;overflow:hidden}
body{font-family:"Mulish",sans-serif;color:var(--body);background:var(--white);position:relative}
.abs{position:absolute}
section,header,footer{position:absolute;left:0;width:1200px}

/* Hero */
.hero{top:0;height:720px;background:linear-gradient(120deg,#12454b 0%,#0e3439 55%,#174a4f 100%)}
.brand{left:85px;top:26px;display:flex;align-items:center;gap:14px;color:var(--white);font-size:36px;font-weight:400;letter-spacing:2px}
.brand-mark{width:44px;height:44px;border:3px solid var(--white)}
.search{left:777px;top:13px;width:194px;height:49px;background:var(--accent);color:var(--white);font-size:13px;letter-spacing:1px;display:flex;align-items:center;justify-content:space-between;padding:0 18px 0 22px}
.btn-contact{left:979px;top:13px;width:135px;height:49px;background:var(--white);color:var(--ink);font-size:16px;display:flex;align-items:center;justify-content:center;font-weight:600}
.nav a{position:absolute;top:80px;color:var(--white);font-size:20px;text-decoration:none}
.frame{background:var(--accent);padding:16px}
.photo{width:100%;height:100%}
.hero-title{left:639px;top:282px;color:var(--accent);font-size:60px;font-weight:900;line-height:1.1}
.hero-sub{left:639px;top:346px;color:var(--white);font-size:42px;font-weight:800}
.btn-touch{left:642px;top:428px;width:160px;height:49px;background:var(--accent);color:var(--white);font-size:16px;display:flex;align-items:center;justify-content:center}
.circle-arrow{width:58px;height:58px}

/* Welcome */
.welcome{top:720px;height:565px}
.welcome h2{position:absolute;left:85px;top:108px;font-family:"Montserrat",sans-serif;font-size:40px;font-weight:800;color:var(--ink)}
.welcome p{position:absolute;left:85px;top:158px;font-size:24px;line-height:40.5px;color:var(--body);white-space:nowrap}
.welcome p strong{color:var(--accent);font-weight:800}
.welcome-tint{left:595px;top:65px;width:202px;height:191px;background:var(--tint)}

/* Services */
.services{top:1285px;height:578px}
.services .band{position:absolute;left:0;top:0;width:1200px;height:435px;background:var(--band)}
.slide-btn{top:-27px;width:71px;height:75px;background:var(--band-dark);display:flex;align-items:center;justify-content:center}
.services h2{position:absolute;left:0;width:1200px;top:45px;text-align:center;color:var(--white);font-family:"Montserrat",sans-serif;font-size:40px;font-weight:800}
.card{top:125px;width:309px;height:453px;background:var(--accent);padding:14px}
.card-inner{background:var(--white);height:100%;position:relative}
.card-photo{height:187px}
.card-icon{position:absolute;left:50%;top:139px;margin-left:-48px;width:96px;height:96px;border-radius:50%;background:#5ff0e6;display:flex;align-items:center;justify-content:center}
.card h3{position:absolute;top:241px;left:10px;right:10px;text-align:center;font-size:18px;font-weight:800;color:var(--ink);line-height:22px}
.card p{position:absolute;left:18px;right:18px;text-align:center;font-size:16.5px;line-height:23px;color:var(--ink)}

/* Newsletter */
.newsletter{top:1961px;left:85px;width:1029px;height:351px;background:var(--accent);padding:23px}
.newsletter-inner{position:relative;background:var(--white);height:100%}
.newsletter h2{position:absolute;left:24px;top:35px;font-family:"Montserrat",sans-serif;font-size:45px;font-weight:800;line-height:46px;color:var(--ink)}
.newsletter h3{position:absolute;left:24px;top:186px;font-family:"Montserrat",sans-serif;font-size:33px;font-weight:800;color:var(--ink)}
.newsletter .note{position:absolute;left:24px;top:238px;font-size:17px;color:var(--body)}
.subscribe{left:503px;top:44px;width:459px;height:209px;background:var(--accent)}
.subscribe .field{position:absolute;left:28px;top:37px;width:403px;height:60px;background:var(--white);font-size:17px;color:#888;display:flex;align-items:center;padding-left:20px}
.subscribe .go{position:absolute;left:28px;top:110px;width:233px;height:60px;background:var(--deep);color:var(--white);font-size:18px;font-weight:800;display:flex;align-items:center;justify-content:center}

/* News */
.news{top:2380px;height:570px}
.news h2{position:absolute;left:85px;top:10px;font-family:"Montserrat",sans-serif;font-size:42px;font-weight:800;color:var(--ink)}
.news h2 span{color:var(--accent)}
.news .lede{position:absolute;left:85px;top:62px;font-size:18px;color:var(--body)}
.article{top:110px;width:488px;height:341px;border:3px solid var(--accent)}
.article .thumb{position:absolute;left:21px;top:30px;width:185px;height:222px}
.article .read{position:absolute;left:21px;top:258px;width:185px;height:48px;background:var(--deep);color:var(--white);font-size:14px;font-weight:800;letter-spacing:1px;display:flex;align-items:center;justify-content:center;gap:10px}
.article .text{position:absolute;left:226px;top:58px;width:245px}
.article h3{font-size:18px;font-weight:800;color:var(--ink);line-height:21px}
.article .link{margin-top:5px;font-size:17px;color:var(--accent);font-weight:600;line-height:19px}
.article p{margin-top:8px;font-size:15px;line-height:23px;color:var(--ink)}
.btn-all{left:488px;top:508px;width:232px;height:58px;background:var(--deep);color:var(--white);font-size:19px;font-weight:800;display:flex;align-items:center;justify-content:center}

/* Booking */
.booking{top:2979px;height:699px;background:linear-gradient(100deg,#1c1d1f 0%,#2b2a28 40%,#1e2326 70%,#2d2b29 100%)}
.booking h2{position:absolute;left:0;width:1200px;top:52px;text-align:center;color:var(--white);font-family:"Montserrat",sans-serif;font-size:43px;font-weight:800;line-height:47px}
.booking h2 span{color:var(--accent)}
.widget{left:273px;top:176px;width:655px;height:491px;background:var(--white);display:flex}
.widget .host{width:327px;height:100%;background:var(--slate);position:relative;color:var(--white)}
.avatar{position:absolute;left:134px;top:32px;width:60px;height:60px;border-radius:50%;border:2px solid #fff;background:linear-gradient(#8c8f95,#3b3d42)}
.host .meet{position:absolute;top:108px;width:100%;text-align:center;font-size:19px}
.host .month{position:absolute;top:140px;width:100%;text-align:center;font-size:18px;font-weight:700}
.cal{position:absolute;left:0;top:185px;width:327px;display:grid;grid-template-columns:repeat(7,46.7px);grid-auto-rows:41px;text-align:center;font-size:11px;align-items:center}
.cal .dow{font-weight:800;font-size:11px;height:20px}
.cal .d{color:#9aa7b8}
.cal .on{color:var(--white);font-weight:800}
.cal .sel{display:inline-flex;width:36px;height:36px;border-radius:50%;background:var(--white);color:var(--slate);align-items:center;justify-content:center;margin:auto}
.widget .slots{position:relative;flex:1}
.slots .lbl{position:absolute;left:25px;font-size:12px;color:#444;font-weight:700}
.slots .bar{position:absolute;left:25px;top:52px;width:278px;height:23px;background:#e4e8ee;font-size:9px;color:#777;display:flex;align-items:center;justify-content:center}
.slots .small{position:absolute;left:25px;font-size:11px;color:#555}
.slots .tz{position:absolute;left:25px;top:208px;width:278px;font-size:10px;color:#3c7bbd;font-weight:700}
.slot{position:absolute;left:27px;width:270px;height:36px;border:1px solid #c9d3df;color:#4b6fa0;font-size:13px;display:flex;align-items:center;justify-content:center}

/* Footer */
.site-footer{top:3678px;height:431px;background:var(--footer);color:var(--white)}
.site-footer .brand{top:72px;font-size:32px}
.site-footer .brand-mark{width:40px;height:40px}
.social{top:146px;left:85px;display:flex;gap:22px}
.social span{width:22px;height:22px;border-radius:50%;background:var(--accent)}
.fcol{top:60px}
.fcol h4{font-size:17px;color:var(--accent);font-weight:700;margin-bottom:8px}
.fcol li{list-style:none;font-size:15px;height:36px;display:flex;align-items:center;gap:8px}
.divider{top:54px;width:1px;height:328px;background:#2f6367}
.loc{font-size:15px;line-height:26px}
.loc .hl{color:var(--accent)}
.bottom-bar{top:4109px;height:82px;background:var(--footer-bar);color:var(--white);text-align:center;font-size:15px}
</style>
</head>
<body>

<header class="hero">
  <div class="abs brand"><span class="brand-mark"></span>qorvanta</div>
  <div class="abs search"><span>Search Any Text</span>
    <svg width="18" height="18" viewBox="0 0 18 18" fill="none" stroke="#fff" stroke-width="2.4"><circle cx="7.5" cy="7.5" r="5.5"/><path d="M11.5 11.5l5 5"/></svg>
  </div>
  <div class="abs btn-contact">Contact Us</div>
  <nav class="nav">
    <a style="left:577px">Home</a><a style="left:690px">Services</a><a style="left:824px">Contact</a><a style="left:954px">About</a><a style="left:1068px">Blog</a>
  </nav>

  <div class="abs frame" style="left:85px;top:176px;width:214px;height:148px"><div class="photo" role="img" aria-label="Engineers reviewing code on a laptop" style="background:linear-gradient(135deg,#4a6c80,#8fb0c0 60%,#c8a88f)"></div></div>
  <div class="abs frame" style="left:333px;top:176px;width:215px;height:294px"><div class="photo" role="img" aria-label="Developer smiling beside a laptop" style="background:linear-gradient(160deg,#c6cdd0,#8b8f92 60%,#2c5d6f)"></div></div>
  <div class="abs frame" style="left:85px;top:361px;width:214px;height:294px"><div class="photo" role="img" aria-label="Hand working on a glowing monitor display" style="background:linear-gradient(150deg,#0e2a4a,#1f6aa8 55%,#0a2036)"></div></div>
  <div class="abs frame" style="left:333px;top:509px;width:215px;height:146px"><div class="photo" role="img" aria-label="Hands on a laptop with digital security icons" style="background:linear-gradient(120deg,#3a3f4a,#6c6f79 50%,#2a4f7e)"></div></div>

  <h1 class="abs hero-title">Reliable Smart</h1>
  <div class="abs hero-sub">Software Engineering</div>
  <div class="abs btn-touch">Get In touch</div>
  <svg class="abs circle-arrow" style="left:641px;top:519px" viewBox="0 0 58 58" fill="none" stroke="#fff" stroke-width="4"><circle cx="29" cy="29" r="26"/><path d="M41 29H18M27 19l-10 10 10 10"/></svg>
  <svg class="abs circle-arrow" style="left:719px;top:519px" viewBox="0 0 58 58" fill="none" stroke="#fff" stroke-width="4"><circle cx="29" cy="29" r="26"/><path d="M17 29h23M31 19l10 10-10 10"/></svg>
</header>

<section class="welcome">
  <h2>WELCOME</h2>
  <p><strong>At Qorvanta,</strong> we craft bespoke software<br>solutions that are not available on the<br>market. By building organizations<br>market-leading products, process<br>automation, legacy system enablement, or<br>advanced intelligent systems, we empower<br>our customers to achieve a competitive</p>
  <div class="abs welcome-tint" role="img" aria-label="Faint decorative backdrop area"></div>
  <div class="abs" style="left:824px;top:80px;width:288px;height:398px;border:4px solid var(--accent)"></div>
  <div class="abs" style="left:647px;top:91px;width:449px;height:374px;background:var(--accent)"></div>
  <div class="abs" role="img" aria-label="Two colleagues collaborating at a computer in a modern office" style="left:670px;top:114px;width:403px;height:329px;background:linear-gradient(135deg,#e9e9e6,#b7bcc0 45%,#46603b 100%)"></div>
</section>

<section class="services">
  <div class="band"></div>
  <div class="abs slide-btn" style="left:966px"><svg width="26" height="40" viewBox="0 0 26 40" fill="none" stroke="#fff" stroke-width="2"><path d="M22 3L4 20l18 17"/></svg></div>
  <div class="abs slide-btn" style="left:1044px"><svg width="26" height="40" viewBox="0 0 26 40" fill="none" stroke="#fff" stroke-width="2"><path d="M4 3l18 17L4 37"/></svg></div>
  <h2>SERVICES</h2>

  <div class="abs card" style="left:89px"><div class="card-inner">
    <div class="card-photo" role="img" aria-label="Team working at desks in an office" style="background:linear-gradient(135deg,#c9ccce,#8d949a 50%,#d8c3b6)"></div>
    <div class="card-icon"><svg width="48" height="48" viewBox="0 0 48 48" fill="none" stroke="#0e3a3e" stroke-width="2.4"><circle cx="24" cy="24" r="8"/><circle cx="24" cy="24" r="14" stroke-dasharray="5 4"/><rect x="6" y="6" width="8" height="8"/><rect x="34" y="34" width="8" height="8"/></svg></div>
    <h3>Enterprise Systems<br>Integration</h3>
    <p style="top:296px">Automate your business processes internally or externally to improve data quality and process efficiency</p>
  </div></div>

  <div class="abs card" style="left:447px"><div class="card-inner">
    <div class="card-photo" role="img" aria-label="Colleagues reviewing charts on a laptop" style="background:linear-gradient(135deg,#e3e5e6,#a9b1b6 50%,#6d6a6a)"></div>
    <div class="card-icon"><svg width="48" height="48" viewBox="0 0 48 48" fill="#0e3a3e"><rect x="6" y="6" width="9" height="9"/><rect x="20" y="6" width="9" height="9"/><rect x="34" y="6" width="9" height="9"/><path d="M10 18l14 10 14-10v6L24 34 10 24z"/><circle cx="24" cy="40" r="5"/></svg></div>
    <h3>Microservices</h3>
    <p style="top:282px">Leverage Microservices Architecture to enable quick deployment, dynamically scalable service performance, team productivity and more</p>
  </div></div>

  <div class="abs card" style="left:803px"><div class="card-inner">
    <div class="card-photo" role="img" aria-label="Hands on a keyboard with glowing circuit graphics" style="background:linear-gradient(135deg,#0b2c48,#1e78a8 55%,#092033)"></div>
    <div class="card-icon"><svg width="48" height="48" viewBox="0 0 48 48" fill="none" stroke="#0e3a3e" stroke-width="2.4"><path d="M8 20L24 9l16 11"/><rect x="10" y="20" width="28" height="16"/><path d="M16 24v8M24 24v8M32 24v8M6 40h36"/></svg></div>
    <h3>Platform engineering</h3>
    <p style="top:280px">For organisations looking to manage the security and cost risks around their cloud infra-structure management for ap-plications</p>
  </div></div>
</section>

<section class="newsletter">
  <div class="newsletter-inner">
    <h2>Australia's Largest<br>health charity<br>implements</h2>
    <h3>Qorvanta API Msg Bus</h3>
    <div class="note">Register to our newsletter to find out more.</div>
    <div class="abs subscribe">
      <div class="field">Enter your email :</div>
      <div class="go">Subscribe Now</div>
    </div>
  </div>
</section>

<section class="news">
  <h2>NEWS <span>&amp; ARTICLES</span></h2>
  <div class="lede">Updates from our industry</div>

  <article class="abs article" style="left:86px">
    <div class="thumb" role="img" aria-label="Woman holding a coffee cup surrounded by digital overlays" style="background:linear-gradient(135deg,#1a4a2c,#4d7b5d 45%,#d9dcd6)"></div>
    <div class="read">Read More <svg width="16" height="12" viewBox="0 0 16 12" fill="none" stroke="#fff" stroke-width="2"><path d="M1 6h13M9 1l5 5-5 5"/></svg></div>
    <div class="text">
      <h3>Ai In Software<br>Engineering</h3>
      <div class="link">10 unexpected ways to use CodeWing Assist</div>
      <p>(CodeWing Blog) CodeWing Assist is widely known for its code generation feature. Learn how the AI assistant's abilities can extend beyond just code generation.</p>
    </div>
  </article>

  <article class="abs article" style="left:624px">
    <div class="thumb" role="img" aria-label="Two developers working together on laptops" style="background:linear-gradient(135deg,#d9d6cf,#6f7d8a 50%,#2b3d52)"></div>
    <div class="read">Read More <svg width="16" height="12" viewBox="0 0 16 12" fill="none" stroke="#fff" stroke-width="2"><path d="M1 6h13M9 1l5 5-5 5"/></svg></div>
    <div class="text">
      <h3>Industry<br>Research</h3>
      <div class="link">PROMTA: A general-purpose framework for prompt optimi-zation</div>
      <p>(Lumen Labs Research) Large language models (LLMs) have revolutionized various tasks, but prompt engineering remains a challenge. Enter PROMTA: an open-source tool that streamlines</p>
    </div>
  </article>

  <div class="abs btn-all">View All News</div>
</section>

<section class="booking" role="img" aria-label="Dimly lit office background behind the booking panel">
  <h2><span>BOOK</span> AN OBLIGATION FREE CONSULTATION<br>WITH OUR LEAD TECHNOLOGIST</h2>
  <div class="abs widget">
    <div class="host">
      <div class="avatar" role="img" aria-label="Portrait of the CTO"></div>
      <div class="meet">Meet with our CTO</div>
      <div class="month">‹ &nbsp; January 2025 &nbsp; ›</div>
      <div class="cal">
        <span class="dow">SUN</span><span class="dow">MON</span><span class="dow">TUE</span><span class="dow">WED</span><span class="dow">THU</span><span class="dow">FRI</span><span class="dow">SAT</span>
        <span></span><span></span><span></span><span class="d">1</span><span class="d">2</span><span class="d">3</span><span class="d">4</span>
        <span class="d">5</span><span class="d">6</span><span class="d">7</span><span class="d">8</span><span class="d">9</span><span class="d">10</span><span class="d">11</span>
        <span class="d">12</span><span class="d">13</span><span class="d">14</span><span><span class="sel">15</span></span><span class="on">16</span><span class="on">17</span><span class="d">18</span>
        <span class="d">19</span><span class="d">20</span><span class="d">21</span><span class="on">22</span><span class="on">23</span><span class="on">24</span><span class="d">25</span>
        <span class="d">26</span><span class="d">27</span><span class="d">28</span><span class="on">29</span><span class="on">30</span><span class="on">31</span><span></span>
      </div>
    </div>
    <div class="slots">
      <div class="lbl" style="top:22px">Meeting duration</div>
      <div class="bar">30 mins</div>
      <div class="lbl" style="top:150px;font-size:11px">What time works best?</div>
      <div class="small" style="top:170px">Showing times for <b>January 15, 2025</b></div>
      <div class="tz">UTC +05:30 New Delhi, Mumbai, Calcutta <span style="float:right;color:#999">˅</span></div>
      <div class="slot" style="top:234px">4:45 am</div>
      <div class="slot" style="top:279px">5:00 am</div>
      <div class="slot" style="top:323px">5:15 am</div>
    </div>
  </div>
</section>

<footer class="site-footer">
  <div class="abs brand"><span class="brand-mark"></span>qorvanta</div>
  <div class="abs social" aria-label="Social media links"><span></span><span></span><span></span><span></span></div>

  <ul class="abs fcol" style="left:382px">
    <h4>Sitemap</h4>
    <li>➜ Home</li><li>➜ Services</li><li>➜ Contact</li><li>➜ About</li><li>➜ Blog</li><li>➜ Contact Us</li>
  </ul>
  <div class="abs divider" style="left:514px"></div>
  <ul class="abs fcol" style="left:545px">
    <h4>Services</h4>
    <li>➜ Enterprise Systems Integration</li><li>➜ Microservices</li><li>➜ Platform Engineering</li><li>➜ Conversation A.I.</li><li>➜ Integration Platform as a Service (iPaaS)</li><li>➜ A.I. Agents</li><li>➜ Real-time Data Stream Processing</li><li>➜ Glidewave</li><li>➜ Technology Expertise</li>
  </ul>
  <div class="abs divider" style="left:880px"></div>
  <div class="abs fcol loc" style="left:899px">
    <h4 style="margin-bottom:4px">Location</h4>
    <div>AUSTRALIA</div>
    <div><span class="hl">➜ Phone :</span> 1800 555 019</div>
    <div style="margin-top:12px"><span class="hl">◈ Head office :</span></div>
    <div style="padding-left:27px">Suite 210, 48 Harbour Lane<br>Melbourne, VIC , 3004</div>
  </div>
</footer>

<div class="abs bottom-bar" style="left:0;width:1200px">
  <div style="position:absolute;top:20px;width:100%">Contact Us &nbsp;| &nbsp; Privacy Policy</div>
  <div style="position:absolute;top:46px;width:100%">Copyright © 2025 &nbsp;Qorvanta</div>
  <svg style="position:absolute;left:1037px;top:24px" width="22" height="28" viewBox="0 0 22 28" fill="none" stroke="var(--accent)" stroke-width="3"><path d="M11 27V3M2 12l9-9 9 9"/></svg>
</div>

</body>
</html>
```